Create a Brochure Design for Harlow Senior Living

Harlow Senior Living is a subsidiary of the Harlow Care Group. This brochure is specifically for the Harlow Senior Living company and brand. Create a 3 panel, front and back, tri-fold brochure. This brochure will be a way to introduce our senior living care home to the community, prospective, clients, and various referral partners. It is modern and state of the art home. Like the home, the brochure must be eye catching, unique in its deliverables (as it doesn’t feel like a care facility) and demonstrate both attention to detail and comfort. Our organization is sophisticated and built around warmth, care and individualized personal attention. The most important aspect of this design is to focus on creating a nurturing, warm, and inviting feel where you would want to put your own loved ones in our care home.
I am open to the creativity of the designer to develop something based on the above criteria; however I would like the design to work well with the existing collateral material. What I mean by that is that while I want everything to have its own personality and stand out as its own brand representative, I still need to be able to tell that the overall design concept stays stylistically inside of the same ‘family’ of existing designed material. Because of this, below I would like for the designer to pull inspiration from the link to our website (Located below) as well as from the attachment of our recently refreshed business cards (Attached). This should allow each design to be unique and creative, while still staying inside of a framework and the feel/style that I am looking for.
Finally, I want all the designers to understand that this brochure design is for a facility where we are responsible to provide care for active, positive, and happy seniors/elders. We have care professionals and staff on-site to provide 24x7, around the clock, care to the elders and geriatric residents as it is needed and required. The photos that are used must represent aging gracefully and with elegance.
Target Market(s)
Seniors(50+), Caring Family Members, Social Workers, Physicians, Hospitals
Industry/Entity Type
Business
Requirements
Must have
- • The company logo must be included.
Nice to have
- Attached you will find a sampling of images related to the long term care industry. Please feel free to use your own images as you see fit. The interior care home pictures are of our actual facility and should be incorporated into the brochure and your design.
Company Information
• Look under the Harlow Senior Living tab at
www.harlowcaregroup.example.

```html
<!DOCTYPE html>
<html lang="en">
<head>
<meta charset="utf-8">
<title>Harlow Senior Living – Tri-fold Brochure</title>
<link href="https://fonts.googleapis.com/css2?family=Ubuntu:ital,wght@0,300;0,400;0,500;0,700;1,300;1,400&family=Sacramento&display=swap" rel="stylesheet">
<style>
  :root{
    --teal:#4e8e8b;
    --teal-mid:#5a9896;
    --teal-soft:#6b9f9d;
    --teal-pale:#79a9a7;
    --teal-ink:#3f8582;
    --grey-brand:#5a5a5a;
    --ink:#4a4a4a;
    --paper:#ffffff;
    --label:#333333;
  }
  *{margin:0;padding:0;box-sizing:border-box}
  html,body{width:785px;height:1200px;overflow:hidden;background:var(--paper)}
  body{position:relative;font-family:"Ubuntu",sans-serif;color:var(--ink)}

  .side-label{position:absolute;font-family:"Sacramento",cursive;font-size:22px;color:var(--label)}
  .fold-label{position:absolute;font-family:"Sacramento",cursive;font-size:15px;color:var(--label)}
  .fold-line{position:absolute;width:0;border-left:1px dashed #555}

  .sheet{position:absolute;left:53px;width:687px;overflow:hidden;background:var(--paper);box-shadow:0 3px 6px rgba(0,0,0,.25)}
  .sheet--exterior{top:80px;height:488px}
  .sheet--interior{top:640px;height:485px}
  .sheet__bands{position:absolute;inset:0;width:100%;height:100%}

  .brand{position:absolute;display:flex;flex-direction:column;align-items:center;text-align:center;font-weight:400}
  .brand__mark{display:block;margin-bottom:7px}
  .brand--group{left:227px;width:230px;top:66px;color:var(--grey-brand);font-size:15px;line-height:16px}
  .brand--group .brand__mark{width:16px;height:16px;background:var(--grey-brand)}
  .brand--living{left:457px;width:230px;top:52px;color:var(--teal-ink);font-size:21px;line-height:23px}
  .brand--living .brand__mark{width:22px;height:22px;background:var(--teal-ink)}
  .brand--inside{left:0;width:229px;top:36px;color:var(--teal-ink);font-size:17px;line-height:19px}
  .brand--inside .brand__mark{width:18px;height:18px;background:var(--teal-ink)}

  .tagline{position:absolute;font-style:italic;font-weight:300;letter-spacing:1.7px;color:#555;font-size:7.8px;line-height:10px}

  /* exterior */
  .contact{position:absolute;left:14px;top:118px;display:flex;align-items:center;gap:12px}
  .contact__icon{width:46px;height:46px;border-radius:50%;background:#fff;box-shadow:0 1px 4px rgba(0,0,0,.35);display:flex;align-items:center;justify-content:center}
  .contact__label{font-size:7px;font-weight:700;color:var(--teal-ink);letter-spacing:.4px}
  .contact__phone{font-size:13px;font-weight:700;color:var(--teal-ink)}

  .panel{position:absolute}
  .features{left:0;top:162px;width:227px;height:306px;background:var(--teal-soft);padding:30px 0 0 40px;color:#fff}
  .features__title{font-size:11.5px;font-weight:700;margin-bottom:12px}
  .features__list{list-style:none;font-size:7.5px;letter-spacing:.2px}
  .features__list li{height:21.2px}
  .features__list li::before{content:"» "}

  .addresses{left:227px;top:162px;width:230px;height:306px;background:var(--teal);color:#fff;text-align:center;font-size:6px;letter-spacing:1.1px;line-height:8px;padding-top:178px}
  .addresses strong{font-weight:700}
  .addresses__rule{width:44px;height:1px;background:rgba(255,255,255,.7);margin:7px auto;position:relative}
  .addresses__rule::after{content:"";position:absolute;left:19px;top:-1.5px;width:4px;height:4px;border-radius:50%;background:#fff}

  .photo{position:absolute}
  .photo--couple{left:457px;top:162px;width:230px;height:306px;
    background:
      radial-gradient(ellipse 60% 45% at 30% 45%,rgba(205,150,120,.75),rgba(205,150,120,0) 70%),
      radial-gradient(ellipse 55% 50% at 80% 40%,rgba(225,180,150,.7),rgba(225,180,150,0) 70%),
      radial-gradient(ellipse 80% 40% at 55% 90%,rgba(225,215,220,.95),rgba(225,215,220,0) 75%),
      linear-gradient(180deg,#c6d8ea 0%,#aec6dc 35%,#c9c3c2 70%,#e4dedd 100%)}

  /* interior */
  .photo--bedroom{left:0;top:115px;width:229px;height:150px;
    background:
      radial-gradient(ellipse 30% 45% at 82% 45%,rgba(240,245,235,.9),rgba(240,245,235,0) 75%),
      radial-gradient(ellipse 25% 50% at 12% 50%,rgba(50,35,30,.85),rgba(50,35,30,0) 75%),
      radial-gradient(ellipse 45% 25% at 45% 72%,rgba(190,150,110,.9),rgba(190,150,110,0) 75%),
      linear-gradient(180deg,#eedf9c 0%,#e4cb84 45%,#a8784a 80%,#7a5232 100%)}
  .photo--lounge{left:229px;top:115px;width:230px;height:150px;
    background:
      radial-gradient(ellipse 45% 25% at 50% 60%,rgba(140,110,85,.9),rgba(140,110,85,0) 75%),
      radial-gradient(ellipse 40% 30% at 40% 20%,rgba(245,235,210,.85),rgba(245,235,210,0) 75%),
      linear-gradient(180deg,#cdb894 0%,#a88c6a 45%,#6f5c4a 72%,#8a8070 100%)}
  .photo--bath{left:459px;top:115px;width:228px;height:150px;
    background:
      radial-gradient(ellipse 30% 45% at 30% 55%,rgba(200,205,210,.8),rgba(200,205,210,0) 75%),
      radial-gradient(ellipse 30% 40% at 70% 55%,rgba(250,248,244,.95),rgba(250,248,244,0) 75%),
      linear-gradient(180deg,#e4c486 0%,#ece3d2 30%,#e1dbd0 70%,#b9ab96 100%)}

  .badge{position:absolute;border-radius:50%;background:var(--teal-pale);color:#fff;font-size:6.5px;font-weight:700;line-height:7.5px;text-align:center;display:flex;align-items:center;justify-content:center;box-shadow:0 0 0 2px #fff}

  .story{top:285px;height:180px;padding-top:18px;color:#fff}
  .story--left{left:0;width:229px;background:var(--teal-mid);padding-left:24px;padding-right:36px}
  .story--centre{left:229px;width:230px;background:var(--teal-pale);padding-left:32px;padding-right:30px}
  .story--right{left:459px;width:228px;background:var(--teal-mid);padding-left:29px;padding-right:28px}
  .story__title{font-size:11.5px;font-weight:700;line-height:13px;margin-bottom:10px}
  .story__lead{font-size:7px;font-weight:700;line-height:10px;margin-bottom:12px}
  .story__body{font-size:7px;font-weight:300;line-height:10px}
</style>
</head>
<body>

<div class="side-label" style="left:55px;top:48px">exterior</div>
<div class="fold-label" style="left:285px;top:56px">fold</div>
<div class="fold-label" style="left:520px;top:56px">fold</div>

<div class="side-label" style="left:55px;top:606px">interior</div>
<div class="fold-label" style="left:292px;top:614px">fold</div>
<div class="fold-label" style="left:525px;top:614px">fold</div>

<section class="sheet sheet--exterior">
  <svg class="sheet__bands" viewBox="0 0 687 488" preserveAspectRatio="none" aria-hidden="true">
    <defs>
      <linearGradient id="metal" x1="0" x2="1" y1="0" y2="0">
        <stop offset="0" stop-color="#555"/><stop offset=".3" stop-color="#8a8a8a"/>
        <stop offset=".55" stop-color="#e6e6e6"/><stop offset=".75" stop-color="#8c8c8c"/>
        <stop offset="1" stop-color="#4f4f4f"/>
      </linearGradient>
    </defs>
    <path d="M0 0H687V14C560 8 420 26 300 22 190 18 90 12 0 16Z" fill="url(#metal)"/>
    <path d="M0 16C90 12 190 18 300 22 420 26 560 8 687 14V20C560 14 420 32 300 28 190 24 90 18 0 22Z" fill="var(--teal)"/>
    <path d="M0 158C120 154 250 164 400 160 520 156 620 158 687 157" stroke="var(--teal)" stroke-width="1.6" fill="none"/>
    <path d="M0 161C120 157 250 167 400 163 520 159 620 161 687 160" stroke="var(--teal)" stroke-width=".8" fill="none"/>
    <path d="M0 470C140 462 300 478 460 470 560 465 640 468 687 466V488H0Z" fill="url(#metal)"/>
  </svg>

  <div class="contact">
    <div class="contact__icon">
      <svg width="22" height="22" viewBox="0 0 24 24" aria-hidden="true"><path d="M6.6 10.8a15.5 15.5 0 0 0 6.6 6.6l2.2-2.2a1 1 0 0 1 1-.25 11.4 11.4 0 0 0 3.6.57 1 1 0 0 1 1 1V20a1 1 0 0 1-1 1A17 17 0 0 1 3 4a1 1 0 0 1 1-1h3.5a1 1 0 0 1 1 1c0 1.25.2 2.45.57 3.6a1 1 0 0 1-.25 1z" fill="#bbb"/></svg>
    </div>
    <div>
      <div class="contact__label">CONTACT US TODAY</div>
      <div class="contact__phone">(808) 555-0142</div>
    </div>
  </div>

  <div class="brand brand--group">
    <span class="brand__mark"></span>
    <span>Harlow<br>Care Group</span>
  </div>
  <p class="tagline" style="left:227px;top:122px;width:230px;text-align:center">Someone you can depend on...<br>Without question.</p>

  <div class="brand brand--living">
    <span class="brand__mark"></span>
    <span>Harlow<br>Senior Living</span>
  </div>

  <div class="panel features">
    <h2 class="features__title">Modern Facilities</h2>
    <ul class="features__list">
      <li>PONDERUM PERICULIS</li>
      <li>MODERATIUS AT PER</li>
      <li>TE EOS MUNDI ACCUSAM</li>
      <li>ADOLESCENS MEI</li>
      <li>EX REQUE ELITR</li>
      <li>EU INANI OPTION MEI</li>
      <li>EI USU PAULO ANIMAL</li>
      <li>SIGNIFERUMQUE</li>
      <li>TEMPOR HENDRERIT ALIQUANDO</li>
      <li>EA DUO, VIDIT DEMOCRITUM</li>
      <li>MEI DIAM SEMPER TIMEAM IUS</li>
    </ul>
  </div>

  <div class="panel addresses">
    <p><strong>Harlow Homecare</strong><br>480 Maple Crest Ave., Suite 210<br>Brookdale, HI 96801</p>
    <div class="addresses__rule"></div>
    <p><strong>Harlow Senior Living</strong><br>72 Linden Shore Road<br>Brookdale, HI 96702</p>
    <div class="addresses__rule"></div>
    <p>Phone: <strong>(808) 555-0142</strong><br>Fax: <strong>(808) 555-0187</strong><br>Email: <strong>info@harlowcare.example</strong><br>Website: <strong>www.harlowcare.example</strong></p>
  </div>

  <div class="photo photo--couple" role="img" aria-label="Photo of a smiling senior couple embracing outdoors under a pale sky"></div>
</section>

<section class="sheet sheet--interior">
  <svg class="sheet__bands" viewBox="0 0 687 485" preserveAspectRatio="none" aria-hidden="true">
    <defs>
      <linearGradient id="metal2" x1="0" x2="1" y1="0" y2="0">
        <stop offset="0" stop-color="#555"/><stop offset=".3" stop-color="#8a8a8a"/>
        <stop offset=".55" stop-color="#e6e6e6"/><stop offset=".75" stop-color="#8c8c8c"/>
        <stop offset="1" stop-color="#4f4f4f"/>
      </linearGradient>
    </defs>
    <path d="M0 0H687V14C560 8 420 26 300 22 190 18 90 12 0 16Z" fill="url(#metal2)"/>
    <path d="M0 16C90 12 190 18 300 22 420 26 560 8 687 14V20C560 14 420 32 300 28 190 24 90 18 0 22Z" fill="var(--teal)"/>
    <path d="M0 111C120 107 250 117 400 113 520 109 620 111 687 110" stroke="var(--teal)" stroke-width="1.6" fill="none"/>
    <path d="M0 268C150 272 300 264 460 268 580 271 640 268 687 268" stroke="var(--teal)" stroke-width="1" fill="none"/>
    <path d="M0 467C140 459 300 475 460 467 560 462 640 465 687 463V485H0Z" fill="url(#metal2)"/>
  </svg>

  <div class="brand brand--inside">
    <span class="brand__mark"></span>
    <span>Harlow<br>Senior Living</span>
  </div>
  <p class="tagline" style="left:517px;top:66px">Someone you can depend on...<br>Without question.</p>

  <div class="photo photo--bedroom" role="img" aria-label="Photo of a furnished bedroom with a large bed and balcony doors"></div>
  <div class="photo photo--lounge" role="img" aria-label="Photo of a spacious lounge with sofas and a rug"></div>
  <div class="photo photo--bath" role="img" aria-label="Photo of an accessible bathroom with shower and grab rails"></div>

  <div class="badge" style="left:180px;top:247px;width:44px;height:44px">Confortable<br>bedrooms</div>
  <div class="badge" style="left:402px;top:101px;width:44px;height:44px">Spacious<br>Lounge<br>Areas</div>
  <div class="badge" style="left:621px;top:226px;width:46px;height:46px">Functional<br>Bathrooms</div>

  <article class="panel story story--left">
    <h3 class="story__title">Lorem ipsum dolor sit amet<br>at nostrum definitiones</h3>
    <p class="story__lead">Ponderum periculis moderatius at per. Te eos mundi accusam adolescens, mei ex reque elitr, eu inani option mei. Ei usu paulo animal signifer­umque. Tempor hendrerit aliquando ea duo, vidit democritum mei te, id diam semper timeam ius.</p>
    <p class="story__body">Rebum illud facilis in nam, ius recteque dissentiunt cu, antiopam splendide abhorreant et mel.<br>Per et populo minimum.</p>
  </article>
  <article class="panel story story--centre">
    <h3 class="story__title">Lorem ipsum dolor sit amet<br>at nostrum definitiones</h3>
    <p class="story__lead">Ponderum periculis moderatius at per. Te eos mundi accusam adolescens, mei ex reque elitr, eu inani option mei. Ei usu paulo animal signifer­umque. Tempor hendrerit aliquando ea duo, vidit democritum mei te, id diam semper timeam ius.</p>
    <p class="story__body">Rebum illud facilis in nam, ius recteque dissentiunt cu, antiopam splendide abhorreant et mel.<br>Per et populo minimum.</p>
  </article>
  <article class="panel story story--right">
    <h3 class="story__title">Lorem ipsum dolor sit amet<br>at nostrum definitiones</h3>
    <p class="story__lead">Ponderum periculis moderatius at per. Te eos mundi accusam adolescens, mei ex reque elitr, eu inani option mei. Ei usu paulo animal signifer­umque. Tempor hendrerit aliquando ea duo, vidit democritum mei te, id diam semper timeam ius.</p>
    <p class="story__body">Rebum illud facilis in nam, ius recteque dissentiunt cu, antiopam splendide abhorreant et mel.<br>Per et populo minimum.</p>
  </article>
</section>

<div class="fold-line" style="left:279px;top:62px;height:530px"></div>
<div class="fold-line" style="left:510px;top:62px;height:530px"></div>
<div class="fold-line" style="left:286px;top:622px;height:522px"></div>
<div class="fold-line" style="left:516px;top:622px;height:522px"></div>

</body>
</html>
```